Letterhead - Pelvarosi Law Group

I receive a fantastic logo from you guys and I'd like to incorporate it into business cards and letterhead. I accidentally approved design No. 58027913 and contacted designer Tarveck, and Tarveck sent me the zip folder for Design No. 58027986, which I very much appreciate.
I'd like to order business cards and letterhead with Design No. 58027986 as soon as possible, but I want to make sure that you incorporate the correct design (attached). I'd also like to provide my information to add (address, phone number, email, fax) but I'm not quite sure how to do it.
The information that I would like on the business cards and letterhead is as follows:
Pelvarosi Law Group
Dorian K. Pelvarosi, Esq.
2741 Halvern Street, Suite 306
San Francisco, CA 94019
Office: (415) 738-0461
Fax: (415) 386-7710
dory@pelvarosilawgroup.com
Thanks in advance for any guidance.
Dory Pelvarosi
Pelvarosi Law Group
(415) 574-8839 (cell)

```html
<!DOCTYPE html>
<html lang="en">
<head>
<meta charset="utf-8">
<title>Pelvarosi Law Group – Letterhead</title>
<link href="https://fonts.googleapis.com/css2?family=Open+Sans:wght@400;600&family=Roboto:wght@400;500&display=swap" rel="stylesheet">
<style>
  :root {
    --backdrop: #e8e8e8;
    --paper: #f8f8f8;
    --ink: #4a4a4a;
    --ink-dark: #222222;
    --accent: #2a86c3;
    --signature-tone: #dfe3ea;
  }
  * { box-sizing: border-box; margin: 0; padding: 0; }
  html, body {
    width: 1200px; height: 795px; overflow: hidden;
    background: var(--backdrop);
  }
  .letterhead {
    position: absolute; left: 331px; top: 18px;
    width: 538px; height: 760px;
    background: var(--paper);
    box-shadow: 0 2px 10px rgba(0,0,0,0.12);
    font-family: "Open Sans", sans-serif;
    color: var(--ink);
  }
  .brand {
    position: absolute; left: 48px; top: 92px;
    display: flex; align-items: center; gap: 8px;
  }
  .brand-mark { width: 10px; height: 10px; background: var(--ink-dark); }
  .brand-name {
    font-size: 15px; font-weight: 600; color: var(--ink-dark);
    letter-spacing: 0.02em;
  }
  .contact {
    position: absolute; left: 330px; top: 52px;
    list-style: none; font-size: 8px; line-height: 11px;
  }
  .contact li { display: flex; align-items: center; gap: 5px; }
  .contact svg { width: 8px; height: 8px; fill: var(--accent); flex: none; }
  .letter-body {
    position: absolute; left: 96px; top: 196px; width: 380px;
    font-size: 8.4px; line-height: 11.6px;
  }
  .salutation { margin-bottom: 12px; }
  .letter-body p.paragraph { margin-bottom: 12px; }
  .closing { margin-top: 4px; }
  .signature {
    display: block; margin: 10px 0 0 30px;
    width: 90px; height: 40px; border-radius: 6px;
    background: var(--signature-tone);
  }
  .footer {
    position: absolute; right: 40px; bottom: 46px;
    text-align: right; font-family: "Roboto", sans-serif;
    font-size: 9px; line-height: 12px; color: var(--ink);
  }
  .footer-firm { font-weight: 500; color: var(--ink-dark); }
</style>
</head>
<body>
  <main class="letterhead">
    <div class="brand">
      <span class="brand-mark"></span>
      <span class="brand-name">Pelvarosi Law Group</span>
    </div>

    <ul class="contact">
      <li><svg viewBox="0 0 10 10"><path d="M2 1h2l1 2.5-1.2 1a5 5 0 0 0 2.7 2.7l1-1.2L10 7v2c0 .6-.4 1-1 1A8 8 0 0 1 1 2c0-.6.4-1 1-1z"/></svg>(415) 738-0461</li>
      <li><svg viewBox="0 0 10 10"><path d="M3 0h4a1 1 0 0 1 1 1v8a1 1 0 0 1-1 1H3a1 1 0 0 1-1-1V1a1 1 0 0 1 1-1zm0 1.5v6h4v-6z"/></svg>(415) 574-8839</li>
      <li><svg viewBox="0 0 10 10"><path d="M2 0h5v3H2zM0 3.5h10V9H0zM2 5v1h2V5zm0 2v1h2V7zm4-2v3h2V5z"/></svg>(415) 386-7710</li>
      <li><svg viewBox="0 0 10 10"><path d="M0 2h10v1L5 6 0 3zm0 2.2 5 3 5-3V8H0z"/></svg>dory@pelvarosilawgroup.com</li>
    </ul>

    <section class="letter-body">
      <p class="salutation">Dear customer,</p>
      <p class="paragraph">Lorem ipsum dolor sit amet, consectetur adipisicing elit, sed do eiusmod tempor incididunt ut labore et dolore magna aliqua. Ut enim ad minim veniam, quis nostrud exercitation ullamco laboris nisi ut aliquip ex ea commodo consequat. Duis aute irure dolor in reprehenderit in voluptate velit esse cillum dolore eu fugiat nulla pariatur. Excepteur sint occaecat cupidatat non proident, sunt in culpa qui officia deserunt mollit anim id est laborum.</p>
      <p class="paragraph">Lorem ipsum dolor sit amet, consectetur adipisicing elit, sed do eiusmod tempor incididunt ut labore et dolore magna aliqua. Ut enim ad minim veniam, quis nostrud exercitation ullamco laboris nisi ut aliquip ex ea commodo consequat. Duis aute irure dolor in reprehenderit in voluptate velit esse cillum dolore eu fugiat nulla pariatur. Excepteur sint occaecat cupidatat non proident, sunt in culpa qui officia deserunt mollit anim id est laborum.</p>
      <p class="paragraph">Lorem ipsum dolor sit amet, consectetur adipisicing elit, sed do eiusmod tempor incididunt ut labore et dolore magna aliqua. Ut enim ad minim veniam, quis nostrud exercitation ullamco laboris nisi ut aliquip ex ea commodo consequat. Duis aute irure dolor in reprehenderit in voluptate velit esse cillum dolore eu fugiat nulla pariatur. Excepteur sint occaecat cupidatat non proident, sunt in culpa qui officia deserunt mollit anim id est laborum.</p>
      <p class="paragraph">Lorem ipsum dolor sit amet, consectetur adipisicing elit, sed do eiusmod tempor incididunt ut labore et dolore magna aliqua. Ut enim ad minim veniam, quis nostrud exercitation ullamco laboris nisi ut aliquip ex ea commodo consequat. Duis aute irure dolor in reprehenderit.</p>
      <p class="closing">Yours Sincerely,</p>
      <span class="signature" role="img" aria-label="Handwritten signature of the sender"></span>
    </section>

    <footer class="footer">
      <p class="footer-firm">Pelvarosi Law Group</p>
      <p>Dorian K. Pelvarosi, Esq. 2741 Halvern Street, Suite 306 San Francisco, CA 94019</p>
    </footer>
  </main>
</body>
</html>
```